DJ company new brochure of services offered

I would like to get a new price sheet made for my company services. Currently it's text only. I would like to add pictures next to each service description also like to add general background colors, and just make it look more attractive overall.

Uplighting - File #4 & file #10
Centerpiece pin-spots - File #15
Wedding Cake Spot - file #13 (can you crop out the logo at the bottom)?
Dance Floor Decal File #5
Gobo Monogram - File # 3
market lighting - file #14
ballroom draping - file #7
Video/projections screens: File #13
Indoor safe sparkler effect (not listed on price sheet yet) File #11
Dancing on a cloud - File #9
Co2 Cannons - File #6

Target Market(s)

bride and grooms

Industry/Entity Type

Entertainment

Font styles to use
Serif

Colors

Designer to choose colors to be used in the design.

Requirements
Must have
• my website is www.brightlinkevents.example
• instagram is: @brightlinkevents.example

```html
<!DOCTYPE html>
<html lang="en">
<head>
<meta charset="utf-8">
<title>Brightlink Events – Wedding Reception Package</title>
<link rel="stylesheet" href="https://fonts.googleapis.com/css2?family=Crimson+Pro:wght@300;400;600&family=Libre+Baskerville:wght@400;700&display=swap">
<style>
  :root {
    --brand-red: #e3252b;
    --band-dark: #3c3c3d;
    --ink: #333333;
    --paper: #ffffff;
    --frame: #2e2e2e;
    --photo-warm: #4a4038;
    --photo-violet: #b9a6c4;
  }
  * { margin: 0; padding: 0; box-sizing: border-box; }
  html, body { width: 848px; height: 1200px; overflow: hidden; background: var(--paper); }
  body { font-family: "Crimson Pro", Georgia, serif; color: var(--ink); }
  .sheet { position: relative; width: 848px; height: 1200px; border: 1px solid #999; background: var(--paper); }
  .abs { position: absolute; }
  .heading { font-family: "Libre Baskerville", Georgia, serif; font-weight: 700; }

  .brand { left: 26px; top: 66px; display: flex; align-items: center; gap: 8px; }
  .brand-dot { width: 12px; height: 12px; border-radius: 50%; background: var(--brand-red); }
  .brand-name { font-family: "Libre Baskerville", Georgia, serif; font-size: 22px; color: var(--brand-red); font-weight: 400; }

  .contact { right: 25px; top: 34px; text-align: right; font-family: "Libre Baskerville", Georgia, serif; font-weight: 700; font-size: 13.5px; line-height: 20.8px; color: var(--ink); }

  .service-band { left: 0; top: 146px; width: 848px; height: 31px; background: var(--band-dark); color: #fff; text-align: center; font-size: 17px; line-height: 31px; letter-spacing: 0.3px; }
  .package-band { left: 0; top: 183px; width: 848px; height: 31px; background: var(--brand-red); color: #fff; font-size: 16.5px; line-height: 31px; padding-left: 28px; }

  .includes { left: 27px; top: 236px; font-size: 16px; font-weight: 300; line-height: 20.5px; }
  .includes p:first-child { margin-bottom: 20.5px; }
  .extras { right: 30px; top: 316px; text-align: right; font-size: 16px; font-weight: 300; line-height: 20.5px; }
  .extras b { font-weight: 600; }
  .extras .gap { height: 40px; }

  .price-card { top: 466px; width: 230px; height: 101px; border: 1.5px solid var(--frame); }
  .price-card .day { height: 30px; background: var(--band-dark); color: #fff; text-align: center; font-family: "Libre Baskerville", Georgia, serif; font-size: 14.5px; line-height: 30px; position: relative; }
  .price-card .tab { position: absolute; left: 4px; top: 0; }
  .price-card .amount { text-align: center; font-family: "Libre Baskerville", Georgia, serif; font-weight: 700; font-size: 14.5px; margin-top: 23px; }

  .addons-tag { left: 0; top: 598px; }
  .addons-title { left: 34px; top: 598px; height: 30px; line-height: 30px; color: #fff; font-size: 16.5px; }

  .photo { }
  .photo-ballroom { left: 25px; top: 644px; width: 398px; height: 265px; background: linear-gradient(180deg, #3b3a37 0%, #55504a 55%, #3f3b36 100%); }
  .photo-drapes { left: 423px; top: 644px; width: 398px; height: 265px; background: linear-gradient(180deg, #d2c3d8 0%, var(--photo-violet) 50%, #9f8fae 100%); }
  .photo-reception { left: 25px; top: 909px; width: 531px; height: 230px; background: linear-gradient(180deg, #3a332e 0%, var(--photo-warm) 50%, #36302c 100%); }
  .photo-sparkler { left: 556px; top: 909px; width: 265px; height: 230px; background: linear-gradient(90deg, #6b6765 0%, #9a9591 60%, #c9c6c2 100%); }

  .menu-text { color: #fff; text-align: center; font-family: "Libre Baskerville", Georgia, serif; text-shadow: 0 1px 2px rgba(0,0,0,0.55); }
  .menu-col { left: 25px; width: 450px; }
  .menu-col .title { font-weight: 700; font-size: 17px; line-height: 21px; }
  .menu-col .detail { font-size: 14.5px; line-height: 20.8px; }
  .col-head { font-size: 18px; }
  .charge { left: 600px; width: 66px; font-size: 15px; line-height: 20.8px; text-align: center; }

  .footnote { left: 0; top: 1148px; width: 848px; text-align: center; font-size: 14px; }
</style>
</head>
<body>
<main class="sheet">
  <div class="abs brand"><span class="brand-dot"></span><span class="brand-name">Brightlink Events</span></div>

  <address class="abs contact" style="font-style:normal">
    # 555.014.2290<br>
    brightlinkevents.example<br>
    hello@brightlinkevents.example<br>
    Instagram- @brightlinkevents.example
  </address>

  <div class="abs service-band heading">DJ &nbsp;|&nbsp; LIGHTING &nbsp;|&nbsp; PRO AUDIO &nbsp;|&nbsp; VISUAL</div>
  <h1 class="abs package-band heading">5 Hour DJ/MC Wedding Reception Package</h1>

  <section class="abs includes">
    <p>This package includes:</p>
    <p>Formally attired &amp; live mixing DJ</p>
    <p>Emcee hosting all announcements</p>
    <p>Powered speaker sound system</p>
    <p>Wireless microphones for toasts speeches</p>
    <p>In-person consultation to discuss event details</p>
    <p>Online access to planning forms &amp; music database</p>
    <p>Up to 6 hours of continuous entertainment</p>
  </section>

  <section class="abs extras">
    <p>Ceremony music (<b>included</b>)</p>
    <p>(includes sound equipment, wireless mic &amp; ceremony music)</p>
    <div class="gap"></div>
    <p>Cocktail hour music (<b>included</b>)</p>
    <p>(includes music in cocktail hour area)</p>
  </section>

  <div class="abs price-card" style="left:26px">
    <div class="day"><svg class="tab" width="8" height="16" viewBox="0 0 8 16"><path d="M0 0H8V16L4 12L0 16Z" fill="#fff"/></svg>Monday-Thursday</div>
    <div class="amount">$1295</div>
  </div>
  <div class="abs price-card" style="left:310px">
    <div class="day"><svg class="tab" width="8" height="16" viewBox="0 0 8 16"><path d="M0 0H8V16L4 12L0 16Z" fill="#fff"/></svg>Friday &amp; Sunday</div>
    <div class="amount">$1395</div>
  </div>
  <div class="abs price-card" style="left:592px">
    <div class="day"><svg class="tab" width="8" height="16" viewBox="0 0 8 16"><path d="M0 0H8V16L4 12L0 16Z" fill="#fff"/></svg>Saturday</div>
    <div class="amount">$1495</div>
  </div>

  <svg class="abs addons-tag" width="563" height="30" viewBox="0 0 563 30"><path d="M0 0H540L563 30H0Z" fill="var(--brand-red)"/></svg>
  <h2 class="abs addons-title heading">Additional services (when booked with DJ package)</h2>

  <div class="abs photo photo-ballroom" role="img" aria-label="Ballroom with warm uplighting and round dining tables"></div>
  <div class="abs photo photo-drapes" role="img" aria-label="Reception hall with white draping, chandeliers and violet uplighting"></div>
  <div class="abs photo photo-reception" role="img" aria-label="Reception room with monogram projected on the dance floor"></div>
  <div class="abs photo photo-sparkler" role="img" aria-label="Couple's first dance with indoor sparkler fountains"></div>

  <div class="abs menu-text menu-col col-head" style="top:683px; width:417px">Services</div>
  <div class="abs menu-text col-head" style="left:580px; top:686px; width:108px">Charges</div>

  <div class="abs menu-text menu-col" style="top:734px">
    <div class="title">Room uplighting (colour of your choice)</div>
    <div class="detail">20 fixtures (med-large room)</div>
    <div class="detail">16 fixtures (med-large room)</div>
    <div class="detail">12 fixtures (med-large room)</div>
  </div>
  <div class="abs menu-text charge" style="top:757px">$400<br>$350<br>$300</div>

  <div class="abs menu-text menu-col" style="top:840px">
    <div class="title">Pin-spot lighting</div>
    <div class="detail">(wedding cake/centerpieces/</div>
    <div class="detail">sweetheart table etc.)</div>
  </div>
  <div class="abs menu-text charge" style="top:843px">$30+</div>

  <div class="abs menu-text menu-col" style="top:926px">
    <div class="title">Dance Floor decal/ Gobo Monogram</div>
    <div class="detail">(bride &amp; groom's names appear on the</div>
    <div class="detail">wall or dance floor)</div>
  </div>
  <div class="abs menu-text charge" style="top:930px">$250+</div>

  <div class="abs menu-text menu-col" style="top:1011px">
    <div class="title">Seamless white dance floor with decal</div>
    <div class="detail">(square or round)</div>
  </div>
  <div class="abs menu-text charge" style="top:1016px; left:595px; width:76px">$1000 +</div>

  <div class="abs menu-text menu-col" style="top:1076px">
    <div class="title">Indoor safe sparkler effect</div>
  </div>

  <p class="abs footnote heading">We offer a wide range of additional services. Please contact us for more info &amp; pricing.</p>
</main>
</body>
</html>
```